Business Card for Ranger Stitch

Target Market(s)

Mining, fleet, 4wd industry

Industry/Entity Type

Business

Requirements
Must have
• Front of card
Logo of Ranger Stitch, the Nut preferrably top right corner and wording which says
"The Classic Bolt Crest Products along bottom right hand corner
Use of the orange logo.
Back of card down left side to include (bullet points )
. Canvas Seat Covers
. Hi - Vis Flags
. Canvas or PVC designs by request.
back of card down right side
Danielle Warbeck
Ph 02 47315928
E ; admin@rangerstitch.com.au
W: www.rangerstitch.com.au
Nice to have
• other designs can also be submitted as we require additional cards.

```html
<!DOCTYPE html>
<html lang="en">
<head>
<meta charset="utf-8">
<title>Ranger Stitch – Business Card</title>
<link rel="stylesheet" href="https://fonts.googleapis.com/css2?family=Open+Sans:wght@300;400;700;800&display=swap">
<style>
  :root {
    --page-bg: #dcdcdc;
    --card-grey: #7b7b7b;
    --brand-orange: #f7941d;
    --text-white: #ffffff;
    --mascot-brown: #8a4a3a;
    --mascot-light: #c98a6e;
  }
  * { box-sizing: border-box; margin: 0; padding: 0; }
  html, body {
    width: 1200px;
    height: 900px;
    overflow: hidden;
    background: var(--page-bg);
    font-family: "Open Sans", Arial, sans-serif;
  }
  .card-sheet {
    position: relative;
    width: 1200px;
    height: 900px;
  }
  .card {
    position: absolute;
    left: 280px;
    width: 640px;
    height: 366px;
    background: var(--card-grey);
    overflow: hidden;
  }
  .card--front { top: 54px; }
  .card--back { top: 480px; }

  .brand-band {
    position: absolute;
    left: 0;
    top: 16px;
    width: 100%;
    height: 112px;
    background: var(--brand-orange);
  }
  .brand-name {
    position: absolute;
    left: 30px;
    top: 30px;
    font-weight: 800;
    font-size: 44px;
    letter-spacing: 1px;
    line-height: 1;
    color: var(--text-white);
    text-transform: uppercase;
  }
  .mascot {
    position: absolute;
    right: 26px;
    top: 4px;
    width: 104px;
    height: 104px;
    border-radius: 50%;
    background: radial-gradient(circle at 40% 40%, var(--mascot-light), var(--mascot-brown));
  }
  .tagline {
    position: absolute;
    right: 24px;
    bottom: 22px;
    font-weight: 700;
    font-size: 20px;
    color: var(--text-white);
  }

  .services {
    position: absolute;
    left: 30px;
    top: 162px;
    list-style: none;
    font-weight: 300;
    font-size: 15px;
    line-height: 30px;
    color: var(--text-white);
  }
  .services li::before {
    content: "";
    display: inline-block;
    width: 7px;
    height: 7px;
    border-radius: 50%;
    background: var(--brand-orange);
    margin-right: 12px;
    vertical-align: middle;
  }
  .divider {
    position: absolute;
    left: 330px;
    top: 158px;
    width: 2px;
    height: 92px;
    background: var(--text-white);
  }
  .contact {
    position: absolute;
    left: 360px;
    top: 162px;
    font-style: normal;
    font-weight: 300;
    font-size: 15px;
    line-height: 23px;
    color: var(--text-white);
  }
</style>
</head>
<body>
<main class="card-sheet">
  <section class="card card--front" aria-label="Card front">
    <div class="brand-band">
      <span class="brand-name">Ranger Stitch</span>
      <div class="mascot" role="img" aria-label="Cartoon nut mascot flexing its arms"></div>
    </div>
    <p class="tagline">The Classic Bolt Crest Products</p>
  </section>

  <section class="card card--back" aria-label="Card back">
    <div class="brand-band">
      <span class="brand-name">Ranger Stitch</span>
      <div class="mascot" role="img" aria-label="Cartoon nut mascot flexing its arms"></div>
    </div>
    <ul class="services">
      <li>Hi - Vis Flags</li>
      <li>Canvas Seat Covers</li>
      <li>Canvas or PVC designs by request</li>
    </ul>
    <div class="divider"></div>
    <address class="contact">
      Danielle Warbeck<br>
      Ph: 02 47315928<br>
      E : admin@rangerstitch.com.au<br>
      W: www.rangerstitch.com.au
    </address>
  </section>
</main>
</body>
</html>
```